Business card design needed for Varrick Medical Practice

We need a new design for our growing medical practice. Our previous design used blue, white and black. I would like to have a design with a baby, child, adult and grandparent on it. We look after a wide range of patients from newborns to 100 year olds.

Industry/Entity Type

Medical

Contact Information for Business Card

Varrick Medical Practice
14 Kestrel Rd Merrin Vale, NSW 2791
Ph 4812 6274 Fax 4831 9527
Dr Maud Pirelli Dr Beatrix Dunmore
Dr Yvonne Kaczmar Dr Estelle Whitcombe
Dr Tom Vasquillo Dr Rex Lund-Patmore
Open Mon- Fri 9-1, 2-5pm
Sat 9-12pm by appointment
web:www.varrickmedical.com.au
email:varrickmedical@quillpost.com

```html
<!DOCTYPE html>
<html lang="en">
<head>
<meta charset="utf-8">
<title>Varrick Medical Practice – Business Card</title>
<link rel="stylesheet" href="https://fonts.googleapis.com/css2?family=Tinos:wght@400&display=swap">
<style>
  :root {
    --stage: #1f1f1f;
    --card: #f7f7f8;
    --blue: #3e55a6;
    --band: #5b6fb9;
    --red: #e11c3a;
    --ink: #1a1a1a;
    --white: #ffffff;
  }
  * { margin: 0; padding: 0; box-sizing: border-box; }
  html, body {
    width: 1200px; height: 1200px; overflow: hidden;
    background: var(--stage);
    font-family: "Tinos", "Times New Roman", serif;
  }
  .card {
    position: absolute; left: 150px; width: 900px; height: 514px;
    overflow: hidden;
  }
  .card-back { top: 60px; background: var(--card); }
  .card-front { top: 626px; }

  .practice { position: absolute; left: 48px; top: 50px; color: var(--blue); font-size: 30px; line-height: 1.15; }
  .contact { position: absolute; left: 48px; top: 150px; font-size: 27px; line-height: 1.25; color: var(--ink); }
  .contact .label { color: var(--red); }

  .doctors { position: absolute; left: 540px; top: 42px; list-style: none; font-size: 27px; line-height: 1.2; color: var(--ink); }
  .doctors li { display: flex; align-items: center; gap: 10px; }
  .doctors .dot { width: 18px; height: 18px; border-radius: 50%; border: 2px solid var(--red); flex: none; }
  .doctors .title { color: var(--blue); }

  .hours { position: absolute; left: 48px; top: 360px; font-size: 27px; color: var(--red); }

  .colour-strip { position: absolute; right: 0; top: 300px; display: flex; height: 22px; }
  .colour-strip span { width: 66px; }
  .colour-strip .b { background: var(--blue); }
  .colour-strip .r { background: var(--red); }

  .front-art { display: block; width: 900px; height: 514px; }
  .brand-name { font-family: "Tinos", "Times New Roman", serif; font-size: 58px; fill: var(--white); }
</style>
</head>
<body>

<section class="card card-back">
  <div class="practice">
    <p>Varrick Medical Practice</p>
    <p>14 Kestrel Rd Merrin Vale, NSW 2791</p>
  </div>

  <div class="contact">
    <p><span class="label">Ph</span> 4812 6274</p>
    <p><span class="label">Fax</span> 4831 9527</p>
    <p><span class="label">web</span>:www.varrickmedical.com.au</p>
    <p><span class="label">email</span>:varrickmedical@quillpost.com</p>
  </div>

  <ul class="doctors">
    <li><span class="dot"></span><span><span class="title">Dr</span> Maud Pirelli</span></li>
    <li><span class="dot"></span><span><span class="title">Dr</span> Beatrix Dunmore</span></li>
    <li><span class="dot"></span><span><span class="title">Dr</span> Yvonne Kaczmar</span></li>
    <li><span class="dot"></span><span><span class="title">Dr</span> Estelle Whitcombe</span></li>
    <li><span class="dot"></span><span><span class="title">Dr</span> Tom Vasquillo</span></li>
    <li><span class="dot"></span><span><span class="title">Dr</span> Rex Lund-Patmore</span></li>
  </ul>

  <div class="colour-strip"><span class="b"></span><span class="r"></span><span class="b"></span><span class="r"></span></div>

  <p class="hours">Open Mon- Fri 9-1 , 2-5pm Sat 9-12pm by appointment</p>
</section>

<section class="card card-front">
  <svg class="front-art" viewBox="0 0 900 514" xmlns="http://www.w3.org/2000/svg">
    <defs>
      <linearGradient id="collage-tone" x1="0" y1="0" x2="1" y2="1">
        <stop offset="0" stop-color="#e9dccf"/>
        <stop offset="0.35" stop-color="#f2ece6"/>
        <stop offset="0.65" stop-color="#dfe3ea"/>
        <stop offset="1" stop-color="#b9c4d6"/>
      </linearGradient>
    </defs>
    <rect class="photo-collage" role="img"
          aria-label="Photo collage of doctors caring for a baby, a child, an adult and an elderly patient"
          x="0" y="0" width="900" height="514" fill="url(#collage-tone)"/>
    <g class="name-band" transform="translate(450 262) rotate(-17)">
      <rect x="-560" y="-46" width="1120" height="92" fill="var(--band)" opacity="0.88"/>
      <circle cx="-330" cy="0" r="30" fill="var(--red)"/>
      <text class="brand-name" x="-282" y="20">Varrick Medical Practice</text>
    </g>
  </svg>
</section>

</body>
</html>
```